VM Tarlo Agency

we need a design for panel, cm 235 x 184 height + roll up as attached sizes, attached find also my logo, my company is www.vmtarloagency.com

Industry/Entity Type

Freight Forwarding

```html
<!DOCTYPE html>
<html lang="en">
<head>
<meta charset="utf-8">
<title>VM Tarlo Agency – Freight Panel</title>
<link rel="stylesheet" href="https://fonts.googleapis.com/css2?family=Oswald:wght@600;700&family=Roboto+Condensed:wght@700&family=Source+Sans+3:wght@700&display=swap">
<style>
  :root{
    --navy:#1f2d5e;
    --red:#e31e24;
    --paper:#f2f2f2;
    --stage:#bdbec0;
    --white:#ffffff;
    --arc:#c9c9cc;
  }
  *{margin:0;padding:0;box-sizing:border-box}
  html,body{width:1200px;height:981px;overflow:hidden;background:var(--stage)}
  .panel{
    position:absolute;left:0;top:21px;width:1220px;height:955px;
    transform:scale(0.98361);transform-origin:0 0;
    background:var(--paper);overflow:hidden;
  }
  .brand{position:absolute;left:52px;top:100px;display:flex;align-items:center;gap:20px}
  .brand-dot{width:66px;height:66px;border-radius:50%;background:var(--navy);flex:none}
  .brand-text{display:flex;flex-direction:column}
  .brand-name{
    font-family:"Oswald",sans-serif;font-weight:700;font-size:56px;line-height:1;
    color:var(--navy);letter-spacing:-0.5px;transform:scaleX(0.86);transform-origin:left;
    white-space:nowrap;
  }
  .brand-tagline{
    font-family:"Roboto Condensed",sans-serif;font-weight:700;font-size:33px;line-height:1;
    color:var(--red);margin:8px 0 0 42px;white-space:nowrap;
  }
  .headline{
    position:absolute;left:760px;top:112px;width:430px;text-align:center;
    font-family:"Oswald",sans-serif;font-weight:600;font-size:40px;line-height:54px;
    color:var(--navy);transform:scaleX(0.86);transform-origin:center;
  }
  .hero-visual{
    position:absolute;left:0;top:262px;width:880px;height:560px;
    background:
      radial-gradient(ellipse 180px 160px at 150px 400px, rgba(240,170,40,.85), rgba(240,170,40,0) 100%),
      radial-gradient(ellipse 220px 170px at 500px 360px, rgba(170,70,40,.7), rgba(170,70,40,0) 100%),
      radial-gradient(ellipse 420px 260px at 360px 220px, rgba(120,160,200,.55), rgba(120,160,200,0) 100%),
      radial-gradient(ellipse 520px 300px at 400px 260px, rgba(200,215,230,.8), rgba(242,242,242,0) 100%);
  }
  .services{position:absolute;left:740px;top:270px;width:460px;height:320px}
  .service{position:absolute;width:150px;text-align:center}
  .service-badge{
    width:86px;height:86px;margin:0 auto;border-radius:50%;
    border:3px solid var(--navy);background:var(--white);
    box-shadow:4px 6px 10px rgba(0,0,0,.18);
    display:flex;align-items:center;justify-content:center;
  }
  .service-badge svg{width:54px;height:54px}
  .service-label{
    margin-top:12px;font-family:"Source Sans 3",sans-serif;font-weight:700;font-size:15px;
    color:var(--navy);letter-spacing:.2px;white-space:nowrap;
  }
  .links{position:absolute;left:0;top:0;width:460px;height:320px}
  .bands{position:absolute;left:0;top:0;width:1220px;height:955px}
  .contact{position:absolute;left:788px;top:826px;width:365px;text-align:center}
  .contact-lead{
    font-family:"Source Sans 3",sans-serif;font-weight:700;font-size:18px;color:var(--white);
  }
  .contact-url{
    display:block;margin-top:14px;height:52px;border-radius:26px;background:var(--red);
    font-family:"Source Sans 3",sans-serif;font-weight:700;font-size:24px;line-height:50px;
    color:var(--white);text-decoration:none;
  }
</style>
</head>
<body>
<main class="panel">
  <div class="hero-visual" role="img" aria-label="Photo montage of a cargo plane, a yellow freight locomotive and a container truck over a faint world map and city skyline"></div>

  <svg class="bands" viewBox="0 0 1220 955" aria-hidden="true">
    <polygon points="0,805 372,883 0,955" fill="var(--red)"/>
    <polygon points="0,955 1220,716 1220,955" fill="var(--navy)"/>
  </svg>

  <header class="brand">
    <span class="brand-dot"></span>
    <div class="brand-text">
      <span class="brand-name">VM TARLO AGENCY</span>
      <span class="brand-tagline">Shipping and Logistics</span>
    </div>
  </header>

  <h1 class="headline">WE MAKE YOUR BUSINESS<br>FLOW CONTINOUSLY</h1>

  <section class="services">
    <svg class="links" viewBox="0 0 460 320" aria-hidden="true">
      <g fill="none" stroke="var(--arc)" stroke-width="1">
        <path d="M92,18 Q170,-8 245,14"/>
        <path d="M252,16 Q330,-10 405,12"/>
        <path d="M92,178 Q170,152 245,174"/>
        <path d="M252,176 Q330,150 405,172"/>
      </g>
      <g fill="var(--red)">
        <circle cx="245" cy="14" r="2.5"/><circle cx="405" cy="12" r="2.5"/>
        <circle cx="92" cy="178" r="2.5"/><circle cx="252" cy="176" r="2.5"/>
      </g>
    </svg>

    <div class="service" style="left:-9px;top:26px">
      <div class="service-badge">
        <svg viewBox="0 0 54 54" fill="var(--red)"><rect x="3" y="24" width="48" height="5" rx="2.5"/><path d="M21 26 L26 10 L30 10 L28 26Z M21 27 L26 42 L30 42 L28 27Z"/><rect x="4" y="20" width="3" height="14"/><circle cx="20" cy="33" r="2"/><circle cx="34" cy="33" r="2"/></svg>
      </div>
      <div class="service-label">AIR FREIGHT</div>
    </div>
    <div class="service" style="left:157px;top:26px">
      <div class="service-badge">
        <svg viewBox="0 0 54 54" fill="var(--red)"><rect x="20" y="8" width="14" height="8" rx="2"/><path d="M14 16 H40 V26 H14Z"/><path d="M8 28 H46 L41 44 Q27 48 13 44Z"/></svg>
      </div>
      <div class="service-label">SEA FREIGHT</div>
    </div>
    <div class="service" style="left:309px;top:26px">
      <div class="service-badge">
        <svg viewBox="0 0 54 54" fill="var(--red)"><rect x="16" y="10" width="22" height="12" rx="2"/><rect x="14" y="22" width="26" height="18" rx="2"/><rect x="18" y="25" width="18" height="6" fill="var(--white)"/><rect x="17" y="40" width="5" height="5"/><rect x="32" y="40" width="5" height="5"/></svg>
      </div>
      <div class="service-label">LAND FREIGHT</div>
    </div>
    <div class="service" style="left:-9px;top:188px">
      <div class="service-badge">
        <svg viewBox="0 0 54 54" fill="var(--red)"><rect x="14" y="8" width="26" height="30" rx="5"/><rect x="18" y="13" width="18" height="9" fill="var(--white)"/><circle cx="20" cy="31" r="2.5" fill="var(--white)"/><circle cx="34" cy="31" r="2.5" fill="var(--white)"/><path d="M16 44 L20 38 H22 L19 44Z M38 44 L34 38 H32 L35 44Z"/><rect x="10" y="44" width="34" height="3"/></svg>
      </div>
      <div class="service-label">RAIL SERVICES</div>
    </div>
    <div class="service" style="left:157px;top:188px">
      <div class="service-badge">
        <svg viewBox="0 0 54 54" fill="var(--red)"><path d="M12 8 H17 L24 38 H42 V41 H22 L15 11 H12Z"/><circle cx="22" cy="44" r="4"/><rect x="24" y="14" width="16" height="22" rx="2"/><path d="M32 18 L36 23 H33 V30 H31 V23 H28Z" fill="var(--white)"/></svg>
      </div>
      <div class="service-label">PROJECT CARGO</div>
    </div>
    <div class="service" style="left:309px;top:188px">
      <div class="service-badge">
        <svg viewBox="0 0 54 54" fill="var(--red)"><path d="M6 20 L27 9 L48 20 V44 H6Z"/><rect x="12" y="24" width="30" height="20" fill="var(--white)"/><rect x="14" y="34" width="7" height="8"/><rect x="23" y="34" width="7" height="8"/><rect x="32" y="34" width="7" height="8"/><rect x="18" y="26" width="8" height="7"/><rect x="28" y="26" width="8" height="7"/></svg>
      </div>
      <div class="service-label">WAREHOUSE</div>
    </div>
  </section>

  <footer class="contact">
    <p class="contact-lead">CONTACT US FOR A FREE QUOTE</p>
    <a class="contact-url" href="#">www.vmtarloagency.com</a>
  </footer>
</main>
</body>
</html>
```